Innovative Consulting Firm Needs New Business Cards and Stationary

Our Innovative Consulting Firm, Larkfield Consulting, is in need of new business cards and stationary designs. We want two-sided cards that incorporate our logo, which is attached. We are looking for something not too formal, but is professional and slick.

Card should have the following information:
Name (ex. Tom Bradley)
Title (ex. Manager)
Address (ex. 24680 Cedar Lane)
Address 2 (ex. Suite 100)
City
State
Zip Code
Mobile
Email

The card should also have our website: www.larkfieldconsulting.example

Industry/Entity Type

Management Consulting

Contact Information for Business Card

Name (ex. Tom Bradley)
Title (ex. Manager)
Address 2 (ex. Suite 100)
City
State
Zip Code
Mobile
Email

Font styles to use
Sans Serif

Requirements
Must have
• The colors on the card must match the colors in the logo. The exact color codes are attached in a pdf.
Nice to have
• The Company's Tagline is "Focused on your Future". This might be nice to incorporate, but not necessary.

```html
<!DOCTYPE html>
<html lang="en">
<head>
<meta charset="utf-8">
<title>Larkfield Consulting – Business Card</title>
<link rel="stylesheet" href="https://fonts.googleapis.com/css2?family=Arimo:wght@400;700&display=swap">
<style>
  :root {
    --bg: #2b2b2b;
    --brand-blue: #1d4f7c;
    --brand-gold: #e1a21a;
    --paper: #f7f7f7;
    --ink: #4a4a4a;
    --ink-blue: #1d3f63;
    --logo-light: #e8eef4;
  }
  * { box-sizing: border-box; margin: 0; padding: 0; }
  html, body { width: 1200px; height: 997px; overflow: hidden; }
  body {
    background: var(--bg);
    font-family: "Arimo", Arial, sans-serif;
    position: relative;
  }
  .card {
    position: absolute;
    width: 540px;
    height: 308px;
    border-radius: 18px;
    overflow: hidden;
    box-shadow: 0 14px 30px rgba(0,0,0,.45);
  }
  .card--front { left: 45px; top: 345px; background: var(--brand-blue); }
  .card--back  { left: 615px; top: 345px; background: var(--paper); }

  .wordmark {
    position: absolute;
    display: flex;
    align-items: center;
    gap: 12px;
    font-weight: 700;
    font-size: 34px;
    letter-spacing: .5px;
    white-space: nowrap;
  }
  .wordmark__dot { width: 16px; height: 16px; border-radius: 50%; background: var(--brand-gold); }
  .card--front .wordmark { left: 50%; top: 50%; transform: translate(-50%, -50%); color: var(--logo-light); }
  .card--back .wordmark { left: 50%; top: 52px; transform: translateX(-50%); color: var(--brand-blue); }

  .holder { position: absolute; right: 26px; top: 140px; text-align: right; }
  .holder__name { color: var(--brand-gold); font-weight: 700; font-size: 20px; }
  .holder__title { color: var(--ink-blue); font-size: 15px; margin-top: 3px; }

  .icon-tab {
    position: absolute; left: 0; top: 156px;
    width: 40px; height: 124px;
    background: var(--brand-blue);
    border-radius: 0 10px 10px 0;
    display: flex; flex-direction: column; justify-content: space-around; align-items: center;
    padding: 4px 0;
  }
  .icon-tab svg { width: 16px; height: 16px; }

  .contacts { position: absolute; left: 58px; top: 158px; list-style: none; }
  .contacts li { color: var(--ink); font-size: 14px; height: 30px; line-height: 30px; white-space: nowrap; }

  .card__bands { position: absolute; left: 0; bottom: 0; width: 540px; height: 64px; }
  .website {
    position: absolute; right: 22px; bottom: 20px;
    color: var(--brand-gold); font-weight: 700; font-size: 14px;
  }
</style>
</head>
<body>
  <section class="card card--front" aria-label="Card front">
    <div class="wordmark"><span class="wordmark__dot"></span>Larkfield Consulting</div>
  </section>

  <section class="card card--back" aria-label="Card back">
    <div class="wordmark"><span class="wordmark__dot"></span>Larkfield Consulting</div>

    <div class="holder">
      <p class="holder__name">Marcus R Delgado</p>
      <p class="holder__title">Managing Partner</p>
    </div>

    <div class="icon-tab">
      <svg viewBox="0 0 16 16" aria-label="Address">
        <path d="M8 1.5 C5 1.5 3.5 3.6 3.5 6 C3.5 9 8 14.5 8 14.5 C8 14.5 12.5 9 12.5 6 C12.5 3.6 11 1.5 8 1.5 Z" fill="#fff"/>
        <circle cx="8" cy="6" r="1.8" fill="var(--brand-blue)"/>
      </svg>
      <svg viewBox="0 0 16 16" aria-label="Fax">
        <rect x="4" y="1.5" width="8" height="4" fill="#fff"/>
        <rect x="1.5" y="5.5" width="13" height="6" rx="1.5" fill="#fff"/>
        <rect x="4" y="10" width="8" height="4.5" fill="#fff" stroke="var(--brand-blue)" stroke-width="1"/>
      </svg>
      <svg viewBox="0 0 16 16" aria-label="Email">
        <rect x="1.5" y="3.5" width="13" height="9" fill="#fff"/>
        <path d="M1.5 3.5 L8 9 L14.5 3.5" fill="none" stroke="var(--brand-blue)" stroke-width="1.2"/>
      </svg>
      <svg viewBox="0 0 16 16" aria-label="Messaging">
        <circle cx="8" cy="8" r="6.5" fill="#fff"/>
      </svg>
    </div>

    <ul class="contacts">
      <li>24680 Cedar Lane, Suite 100</li>
      <li>+1 (555) 014-2290</li>
      <li>marcusd@larkfieldconsulting.example</li>
      <li>/larkfieldconsulting</li>
    </ul>

    <svg class="card__bands" viewBox="0 0 540 64" aria-hidden="true">
      <path d="M0 52 L262 44 L248 64 L0 64 Z" fill="var(--brand-gold)"/>
      <path d="M262 12 Q266 2 280 2 L540 2 L540 64 L240 64 Z" fill="var(--brand-blue)"/>
    </svg>
    <p class="website">www.larkfieldconsulting.example</p>
  </section>
</body>
</html>
```